Tolsán & Quiroga, Vendrexa exclusive agency

I need you to make me designs for my company's business cards, we are an Vendrexa Exclusive Agency.

Target Market(s)

Business

Contact Information for Business Card

Debe contener:
- El logo de la Agencia.
- El logo de Vendrexa
- El nombre de la empresa Tolsán & Quiroga
- La pag web www.tolsanquiroga-ejemplo.com y el código QR de la web
- El Facebook corporativo: facebook.com/vendrexa.seguros.tolsanquirogasl
- tlf: 900 47 52 36
- Móvil: 612 90 24 77
Mi nombre: Tomás Lorente Quiroga

Oficinas: Cl. Almendro, núm. 482, 3°, Oficina 14, 32005, Ourense
Cl. Fermín Otero, núm. 9, 4° Oficinas A-B, 36214, Vigo.

El correo electrónico: info@tolsanquiroga-ejemplo.com

Font styles to use
Sans Serif

Requirements
Must have
• You must maintain corporate colors. Can be on blue background or on white background. Part ahead: - The Agency logo should go in the upper left. - The Vendrexa logo should be smaller in the upper right - p. Web and Facebook. - Personal data, name, telephones and mail Back: - QR code of the web. - Offices and location of the same It will be valued that they play with the corporate colors in letters and design, besides introducing watermarks of the logo in the back part.
Nice to have
• The letter in Tahoma or Arial

```html
<!DOCTYPE html>
<html lang="es">
<head>
<meta charset="utf-8">
<title>Tolsán &amp; Quiroga — Tarjetas de visita</title>
<link rel="stylesheet" href="https://fonts.googleapis.com/css2?family=Montserrat:wght@600;800&family=Open+Sans:wght@600&family=Arimo:wght@400;700&display=swap">
<style>
  :root {
    --stage: #141414;
    --brand-blue: #174a8b;
    --brand-green: #7cc242;
    --paper: #ffffff;
    --ink: #3a3a3a;
    --soft-white: rgba(255, 255, 255, 0.85);
  }
  * { box-sizing: border-box; margin: 0; padding: 0; }
  html, body { width: 1200px; height: 1200px; overflow: hidden; }
  body {
    background: var(--stage);
    display: flex;
    flex-direction: column;
    align-items: center;
    justify-content: center;
    gap: 60px;
  }
  .card {
    position: relative;
    width: 900px;
    height: 500px;
    overflow: hidden;
  }

  /* Shared brand lockup */
  .brand-lockup {
    position: absolute;
    display: flex;
    align-items: center;
    gap: 18px;
  }
  .brand-mark {
    width: 56px; height: 56px;
    background: var(--brand-green);
    flex: none;
  }
  .brand-name {
    font-family: "Montserrat", sans-serif;
    font-weight: 800;
    font-size: 52px;
    line-height: 1;
    color: var(--brand-green);
    white-space: nowrap;
  }
  .brand-tagline {
    font-family: "Montserrat", sans-serif;
    font-weight: 600;
    font-size: 22px;
    letter-spacing: 4px;
    margin-top: 8px;
    color: var(--paper);
    white-space: nowrap;
  }

  /* Reverse side */
  .card--back { background: var(--brand-blue); }
  .card--back .brand-lockup { left: 178px; top: 130px; }
  .office-list {
    position: absolute;
    left: 60px;
    bottom: 50px;
    list-style: none;
    font-family: "Arimo", sans-serif;
    font-size: 18px;
    line-height: 1.45;
    color: var(--soft-white);
  }
  .office-list li { display: flex; align-items: flex-start; gap: 10px; margin-top: 10px; }
  .office-city { font-weight: 700; color: var(--brand-green); }
  .web-qr {
    position: absolute;
    right: 60px;
    bottom: 50px;
    width: 120px;
    height: 120px;
    background: var(--paper);
    border: 10px solid var(--paper);
    outline: 3px solid var(--brand-green);
  }

  /* Front side */
  .card--front { background: var(--paper); }
  .card--front .brand-lockup { left: 60px; top: 60px; }
  .card--front .brand-name { font-size: 46px; }
  .card--front .brand-tagline { font-size: 19px; letter-spacing: 3.5px; color: var(--brand-blue); }
  .card--front .brand-mark { width: 50px; height: 50px; background: var(--brand-blue); }

  .partner-name {
    position: absolute;
    right: 60px;
    top: 48px;
    font-family: "Montserrat", sans-serif;
    font-weight: 800;
    font-size: 24px;
    color: var(--brand-blue);
  }

  .holder-name {
    position: absolute;
    right: 70px;
    top: 196px;
    font-family: "Open Sans", sans-serif;
    font-weight: 600;
    font-size: 36px;
    letter-spacing: -0.5px;
    color: var(--brand-blue);
  }
  .holder-accent {
    position: absolute;
    right: 0;
    top: 198px;
    width: 40px;
    height: 48px;
    background: var(--brand-green);
  }
  .contact-list, .social-list {
    position: absolute;
    list-style: none;
    font-family: "Arimo", sans-serif;
    font-size: 20px;
    color: var(--ink);
  }
  .contact-list { right: 40px; top: 262px; }
  .social-list { left: 60px; bottom: 100px; }
  .contact-list li, .social-list li {
    display: flex;
    align-items: center;
    gap: 12px;
    margin-bottom: 10px;
  }
  .contact-list li { justify-content: flex-end; }
  .icon { width: 22px; height: 22px; flex: none; }
  .footer-rule {
    position: absolute;
    left: 0; right: 0;
    bottom: 80px;
    height: 4px;
    background: var(--brand-green);
  }
  .footer-band {
    position: absolute;
    left: 0; right: 0; bottom: 0;
    height: 70px;
    background: var(--brand-blue);
  }
</style>
</head>
<body>

  <section class="card card--back" aria-label="Reverso de la tarjeta">
    <div class="brand-lockup">
      <span class="brand-mark"></span>
      <div>
        <div class="brand-name">Tolsán &amp; Quiroga</div>
        <div class="brand-tagline">Agencia exclusiva Vendrexa</div>
      </div>
    </div>

    <ul class="office-list">
      <li>
        <svg class="icon" viewBox="0 0 22 22" aria-hidden="true">
          <path d="M11 2a6 6 0 0 0-6 6c0 4.5 6 12 6 12s6-7.5 6-12a6 6 0 0 0-6-6z" fill="#7cc242"/>
          <circle cx="11" cy="8" r="2.2" fill="#174a8b"/>
        </svg>
        <span>Cl. Almendro, núm. 482, 3°, Oficina 14, 32005, <span class="office-city">Ourense</span></span>
      </li>
      <li>
        <svg class="icon" viewBox="0 0 22 22" aria-hidden="true">
          <path d="M11 2a6 6 0 0 0-6 6c0 4.5 6 12 6 12s6-7.5 6-12a6 6 0 0 0-6-6z" fill="#7cc242"/>
          <circle cx="11" cy="8" r="2.2" fill="#174a8b"/>
        </svg>
        <span>Cl. Fermín Otero, núm. 9, 4° Oficinas A-B, 36214, <span class="office-city">Vigo</span></span>
      </li>
    </ul>

    <div class="web-qr" role="img" aria-label="Código QR de www.tolsanquiroga-ejemplo.com"></div>
  </section>

  <section class="card card--front" aria-label="Anverso de la tarjeta">
    <div class="brand-lockup">
      <span class="brand-mark"></span>
      <div>
        <div class="brand-name">Tolsán &amp; Quiroga</div>
        <div class="brand-tagline">Agencia exclusiva Vendrexa</div>
      </div>
    </div>

    <div class="partner-name">Vendrexa</div>

    <h1 class="holder-name">TOMÁS LORENTE QUIROGA</h1>
    <span class="holder-accent"></span>

    <ul class="contact-list">
      <li>900 47 52 36
        <svg class="icon" viewBox="0 0 22 22" aria-hidden="true">
          <rect x="1" y="1" width="20" height="20" rx="3" fill="#174a8b"/>
          <path d="M7 6c-1 1-1 3 1 6s4 4 6 4l1.5-1.5-2-2-1.2.8c-1-.5-2-1.5-2.6-2.6l.8-1.2-2-2z" fill="#fff"/>
        </svg>
      </li>
      <li>612 90 24 77
        <svg class="icon" viewBox="0 0 22 22" aria-hidden="true">
          <rect x="1" y="1" width="20" height="20" rx="3" fill="#174a8b"/>
          <rect x="7.5" y="4.5" width="7" height="13" rx="1.2" fill="none" stroke="#fff" stroke-width="1.5"/>
          <circle cx="11" cy="15" r="0.9" fill="#fff"/>
        </svg>
      </li>
      <li>info@tolsanquiroga-ejemplo.com
        <svg class="icon" viewBox="0 0 22 22" aria-hidden="true">
          <rect x="2" y="2" width="18" height="18" rx="2" fill="none" stroke="#174a8b" stroke-width="3"/>
        </svg>
      </li>
    </ul>

    <ul class="social-list">
      <li>
        <svg class="icon" viewBox="0 0 22 22" aria-hidden="true">
          <rect x="1" y="1" width="20" height="20" rx="3" fill="#174a8b"/>
        </svg>
        tolsán &amp; quiroga
      </li>
      <li>
        <svg class="icon" viewBox="0 0 22 22" aria-hidden="true">
          <rect x="1" y="1" width="20" height="20" rx="4" fill="#174a8b"/>
          <circle cx="11" cy="11" r="6" fill="none" stroke="#fff" stroke-width="1.5"/>
          <path d="M5 11h12M11 5c-3 3-3 9 0 12M11 5c3 3 3 9 0 12" fill="none" stroke="#fff" stroke-width="1.2"/>
        </svg>
        www.tolsanquiroga-ejemplo.com
      </li>
    </ul>

    <span class="footer-rule"></span>
    <span class="footer-band"></span>
  </section>

</body>
</html>
```